Updated website design needed for Radiology Group, Pinecrest Valley Imaging Partners

Clean, uncluttered, updated design needed for top regional Radiology Center. Focus on personal, patient oriented design, (not clinical). Should be simple and easy to navigate, with clear CTAs. Use blues, greens and photos of people in the Central Oregon outdoors.
Uncoded, PSD design only. 2 pages: Home page and one example interior page.
reference current site: http://www.pvipxq.com/
Sites they like:
http://www.hollowbrookscan.com/
http://www.mdlq.net/handler.cfm?event=practice,main
http://www.elmtidejoint.com/

Industry/Entity Type

Medical Imaging

Number of Pages Required

2 page

Font styles to use
Sans Serif

Requirements
Must have
• Personal and patient friendly.
• Lots of white space, clean and uncluttered. Clear CTAs, such as: Patient Bill Pay, Make an Appointment, Meet Our Doctors
• Use copy and contact information from the current site.
• Use outdoor images from Central Oregon, late Winter/ Spring (snow, light colors, spring green, for example)
• Include one example interior page, either Your Exam or Meet Our Doctors
Nice to have
• The client likes:
• Meet Our Doctors slider section, and big, easy to navigate Information Center on www.elmtidejoint.com
• The personal feel of the Your Exam section on www.hollowbrookscan.com
• Blues and Greens, outdoorsy imagery
Should not have
• The client does not like:
• complex drop down menus
• clinical feel
• Do not use lorum ipsum or dummy text.
• Do not use outdoor images from other regions. Do not use Summer (hot, poolside) or Fall (red/orange leaves) images.

```html
<!DOCTYPE html>
<html lang="en">
<head>
<meta charset="utf-8">
<title>Pinecrest Valley Imaging Partners</title>
<link rel="stylesheet" href="https://fonts.googleapis.com/css2?family=Andika&family=Arimo:wght@400;700&display=swap">
<style>
  :root {
    --white: #ffffff;
    --ink: #1c1d26;
    --brand: #3c3f55;
    --brand-mark: #8f93c4;
    --nav-top: #f4f4f4;
    --nav-bottom: #d9d9d9;
    --nav-divider: #a9a9a9;
    --hero-sky: #7c8392;
    --hero-mid: #4f5564;
    --hero-snow: #9da3ae;
    --hero-meadow: #4f5a3e;
    --hero-ground: #5b4d37;
    --circle: rgba(120, 124, 138, 0.55);
    --band-light: #dbe5f1;
    --panel: #a3abd0;
    --button: #d4daf1;
    --button-edge: #8a90b0;
    --footer: #5c6169;
  }
  * { margin: 0; padding: 0; box-sizing: border-box; }
  html, body { width: 1200px; height: 1200px; overflow: hidden; background: var(--white); }
  .page { position: relative; width: 1200px; height: 1200px; font-family: "Arimo", Arial, sans-serif; color: var(--ink); }

  .site-header { position: absolute; top: 0; left: 0; width: 1200px; height: 110px; background: var(--white); }
  .brand { position: absolute; left: 120px; top: 14px; display: flex; align-items: center; gap: 16px; }
  .brand-mark { width: 78px; height: 78px; background: var(--brand-mark); }
  .brand-name { font-family: "Andika", sans-serif; font-size: 27px; line-height: 1.15; color: var(--brand); width: 230px; }

  .main-nav { position: absolute; top: 110px; left: 0; width: 1200px; height: 56px;
    background: linear-gradient(var(--nav-top), var(--nav-bottom)); box-shadow: 0 3px 5px rgba(0,0,0,0.25); }
  .nav-item { position: absolute; top: 0; height: 56px; display: flex; align-items: center; justify-content: center;
    font-family: "Andika", sans-serif; font-size: 20px; color: var(--ink); }
  .nav-divider { position: absolute; top: 4px; width: 2px; height: 48px; background: var(--nav-divider); }

  .hero { position: absolute; top: 172px; left: 0; width: 1200px; height: 570px; overflow: hidden;
    background: linear-gradient(180deg, var(--hero-sky) 0%, var(--hero-mid) 30%, var(--hero-snow) 52%, var(--hero-mid) 62%, var(--hero-meadow) 78%, var(--hero-ground) 100%); }
  .hero-circle { position: absolute; left: 378px; top: 28px; width: 444px; height: 444px; border-radius: 50%; background: var(--circle); }
  .hero-title { position: absolute; top: 58px; left: 0; width: 1200px; text-align: center;
    font-family: "Andika", sans-serif; font-size: 31px; line-height: 36px; color: var(--white); }
  .hero-text { position: absolute; top: 216px; left: 450px; width: 300px; text-align: center;
    font-family: "Andika", sans-serif; font-size: 19px; line-height: 24px; color: var(--white); }
  .hero-rule { position: absolute; top: 356px; left: 462px; width: 300px; height: 1px; background: rgba(255,255,255,0.6); }

  .band-light { position: absolute; top: 744px; left: 0; width: 1200px; height: 40px; background: var(--band-light); }
  .features { position: absolute; top: 782px; left: 0; width: 1200px; height: 286px; background: var(--panel);
    box-shadow: 0 5px 8px rgba(0,0,0,0.3); }
  .feature { position: absolute; top: 26px; width: 270px; }
  .feature-title { font-size: 25px; font-weight: 700; text-decoration: underline; text-underline-offset: 3px; margin-bottom: 10px; }
  .feature-text { font-size: 19px; font-weight: 700; line-height: 25px; color: #22232c; }
  .feature-button { position: absolute; top: 212px; width: 163px; height: 46px; background: var(--button);
    border: 1px solid var(--button-edge); box-shadow: 2px 3px 4px rgba(0,0,0,0.35);
    display: flex; align-items: center; justify-content: center; font-size: 19px; font-weight: 700; color: #2e3040; }
  .band-base { position: absolute; top: 1068px; left: 0; width: 1200px; height: 62px; background: var(--band-light); }
  .site-footer { position: absolute; top: 1134px; left: 0; width: 1200px; height: 66px; background: var(--footer);
    border-top: 3px solid #3e4248; }
</style>
</head>
<body>
<div class="page">
  <header class="site-header">
    <div class="brand">
      <div class="brand-mark"></div>
      <div class="brand-name">Pinecrest Valley Imaging Partners</div>
    </div>
  </header>

  <nav class="main-nav">
    <div class="nav-item" style="left:0;width:178px">About Us</div>
    <div class="nav-divider" style="left:177px"></div>
    <div class="nav-item" style="left:179px;width:277px">Radiology Services</div>
    <div class="nav-divider" style="left:455px"></div>
    <div class="nav-item" style="left:457px;width:246px">Meet the Doctors</div>
    <div class="nav-divider" style="left:702px"></div>
    <div class="nav-item" style="left:704px;width:286px">Patient Information</div>
    <div class="nav-divider" style="left:989px"></div>
    <div class="nav-item" style="left:991px;width:209px">Contact Us</div>
  </nav>

  <section class="hero">
    <div role="img" aria-label="Snow-capped mountain range above a spring meadow with a small stream" style="position:absolute;inset:0"></div>
    <div class="hero-circle"></div>
    <h1 class="hero-title" style="font-weight:400">Welcome to<br>Pinecrest Valley<br>Imaging Partners</h1>
    <p class="hero-text">a diagnostic imaging corporation providing professional services to Central and Eastern Oregon hospitals and clinics.</p>
    <div class="hero-rule"></div>
  </section>

  <div class="band-light"></div>

  <section class="features">
    <div class="feature" style="left:65px">
      <h2 class="feature-title">The Physicians</h2>
      <p class="feature-text">Discover how Pinecrest Valley Imaging’s expertise, collaborative measures, and depth of recources work for you.</p>
    </div>
    <a class="feature-button" style="left:84px">Learn More</a>

    <div class="feature" style="left:353px">
      <h2 class="feature-title">Urgent Care</h2>
      <p class="feature-text">Pinecrest Valley Imaging offers extended hours in several locations for your urgent care needs. Find a location near you.</p>
    </div>
    <a class="feature-button" style="left:368px">Care Hours</a>

    <div class="feature" style="left:654px">
      <h2 class="feature-title">Find Us</h2>
      <p class="feature-text">Find an office near you. We are focused on bringing our premium care to your community.</p>
    </div>
    <a class="feature-button" style="left:660px">Find Us</a>

    <div class="feature" style="left:954px;width:220px">
      <h2 class="feature-title">Patient Portal</h2>
      <p class="feature-text">Send emails, request appointments, lab results and RX refills from anywhere in the world.</p>
    </div>
    <a class="feature-button" style="left:963px">Log In</a>
  </section>

  <div class="band-base"></div>
  <footer class="site-footer"></footer>
</div>
</body>
</html>
```